Marlow Crest Group (Real Estate and Investment)

A high end, clean design.
We are a real estate company with sales, asset management and investment divisions. We want to use a black and white scheme which is really high end feel. The back of the card can just be the logo (black background with the white writing) as we will probably emboss this when we print)

Target Market(s)

High level investors, high end houses for sale

Industry/Entity Type

Business

Contact Information for Business Card

Name, position, phone number and email address
Glen Varley, Managing Director, 0437259064 and glen@marlowcrest-example.com.au

Requirements
Must have
• Back of the card to be the black background with the white writing (as per the attached images). Would like the capacity to emboss the writing and logo

```html
<!DOCTYPE html>
<html lang="en">
<head>
<meta charset="utf-8">
<title>Marlow Crest Group — Business Card</title>
<link rel="stylesheet" href="https://fonts.googleapis.com/css2?family=Open+Sans:wght@400;600&display=swap">
<style>
  :root {
    --stage: #000000;
    --card: #ffffff;
    --card-dark: #0b0b0b;
    --card-edge: #3a3a3a;
    --ink: #1a1a1a;
    --ink-soft: #2b2b2b;
    --ink-light: #ffffff;
  }
  * { margin: 0; padding: 0; box-sizing: border-box; }
  html, body {
    width: 1200px;
    height: 900px;
    overflow: hidden;
    background: var(--stage);
    font-family: "Open Sans", Arial, sans-serif;
    color: var(--ink);
  }
  .stage { position: relative; width: 1200px; height: 900px; }

  .card {
    position: absolute;
    width: 477px;
    height: 293px;
  }
  .card-front {
    left: 116px; top: 275px;
    background: var(--card);
    border-radius: 0 50px 0 50px;
  }
  .card-back {
    left: 622px; top: 276px; height: 292px;
    background: var(--card-dark);
    border: 1px solid var(--card-edge);
    border-radius: 50px 0 50px 0;
    color: var(--ink-light);
  }

  .brand { position: absolute; text-align: center; }
  .brand-circle {
    display: block;
    margin: 0 auto;
    border: 1.6px solid currentColor;
    border-radius: 50%;
  }
  .brand-name {
    display: block;
    font-weight: 400;
    letter-spacing: 0.01em;
    white-space: nowrap;
  }

  .card-front .brand { right: 20px; top: 44px; text-align: right; color: var(--ink); }
  .card-front .brand-circle { width: 86px; height: 86px; margin: 0 15px 0 auto; }
  .card-front .brand-name { font-size: 20px; margin-top: 12px; }

  .card-back .brand { left: 0; right: 0; top: 74px; color: var(--ink-light); }
  .card-back .brand-circle { width: 102px; height: 102px; }
  .card-back .brand-name { font-size: 24px; margin-top: 20px; }

  .holder { position: absolute; left: 28px; top: 192px; }
  .holder-name { font-size: 17px; font-weight: 600; line-height: 22px; }
  .holder-role { font-size: 13px; line-height: 18px; color: var(--ink-soft); }

  .contact {
    position: absolute;
    right: 20px;
    top: 229px;
    list-style: none;
    text-align: right;
    font-size: 13px;
    line-height: 20px;
  }
  .contact li { display: flex; align-items: center; justify-content: flex-end; gap: 5px; }
  .contact svg { width: 10px; height: 10px; fill: var(--ink); }
</style>
</head>
<body>
<main class="stage">
  <section class="card card-front" aria-label="Card front">
    <div class="brand">
      <span class="brand-circle" aria-hidden="true"></span>
      <span class="brand-name">MARLOW CREST GROUP</span>
    </div>
    <div class="holder">
      <p class="holder-name">Glen Varley</p>
      <p class="holder-role">Managing Director</p>
    </div>
    <ul class="contact">
      <li>0437259064
        <svg viewBox="0 0 24 24" aria-hidden="true"><path d="M6.6 10.8a15.1 15.1 0 0 0 6.6 6.6l2.2-2.2c.3-.3.7-.4 1-.2 1.1.4 2.3.6 3.6.6.6 0 1 .4 1 1V20c0 .6-.4 1-1 1A17 17 0 0 1 3 4c0-.6.4-1 1-1h3.5c.6 0 1 .4 1 1 0 1.3.2 2.5.6 3.6.1.3 0 .7-.2 1z"/></svg>
      </li>
      <li>glen@marlowcrest-example.com.au
        <svg viewBox="0 0 24 24" aria-hidden="true"><path d="M2 5h20v14H2z"/><path d="M3 6l9 7 9-7" fill="none" stroke="#fff" stroke-width="2"/></svg>
      </li>
    </ul>
  </section>

  <section class="card card-back" aria-label="Card back">
    <div class="brand">
      <span class="brand-circle" aria-hidden="true"></span>
      <span class="brand-name">MARLOW CREST GROUP</span>
    </div>
  </section>
</main>
</body>
</html>
```